Our business name is Tremlow Skyworks Pty Ltd and we already have a logo. We would like the same colours that appear in our logo on our marketing material. I have attached our logo for colour consistency. We need a brochure designed that promotes our aerial photography and aerial imaging services. We'd like to use the brochure for electronic marketing purposes in an effort to attract a new client base. We are a new start up business so funds are fairly scarce. We use sophisticated UAV (unmanned aerial vehicle) or RPA - remotely piloted aircraft technology) that captures beautiful video and still images.
Our services are suitable for many types of industries and applications. We have identified at least 10 market sectors ranging, infrastructure inspections such as: gas pipelines, chemical and petrol storage facilities, pipeline and power line inspections, Archeological and geological surveys, vegetation mapping, wildlife surveys, agriculture and horticulture surveys, high end real estate, sport and event marketing. Our plan is to create a series of brochures (1) for each industry to help us market our business.

Our first brochure will focus on environmental management and compliance. We will target other industries down the track. These industries would see our service as helping them meet their compliance and auditing requirements.
We have a brochure that we put together containing words and some (very boring) format. As this will be one of a series of brochures, we'd like to colour code the industries for easy identification. (perhaps a green tab) in the corner to distinguish between our brochures. We have attached our boring brochure as a starting point. If we like the design there will be more work to follow. We want to be able to standardise the format for the other industries we will target. We anticipate needing another 6-8 brochures over the course of the next 2 months.
Updates

I have received questions regarding brochure size.  Apologies, I should have indicated in my posting previously.  The brochure is A3 landscape size so it can be folded in half to make 4 A4 pages.  We need to keep printing costs down so the content needs to be  within 4 pages.  I'm about to make some minor changes to the content to try to reduce the amount of text cause I can see this may be a problem.  Look forward to receiving your design. Thanking you in advance for your great work!

Re: Brochure Tremlow Environmental Compliance and Monitoring Services

I have reduced the amount of text contained in the original version of the brochure making it more succinct and less wordy.  Could you use the least amount of space because we want to be able to use this brochure as both electric marketing and print based.  I have also included additional photos which will give you more to work with.  Thank you for your work in advance!  Regards Marisa 

PLEASE NOTE - TEXT HAS BEEN UPDATED (REDUCED TEXT IN BROCHURE). COULD YOU REFER TO VERSION 2 OF TREMLOW ENVIRONMENTAL COMPLIANCE AND MONITORING SERVICES BROCHURE UPDATED FRIDAY 17TH.

Thanks Marisa 

Hi talented designers working on the Tremlow Brochure for Environmental Compliance and Monitoring.  I have been asked to upload the EPS version of Tremlow Logo.  I have just done so.

Regards
Marisa 

Hi all, to assist you with the design concept. I feel I need to clarity a number of points.  We are a new technology driven business.  No one else is conducting environmental surveys using this type of sophisticated equipment. We are in the business of providing clients with visual data (aerial images). Could you include grab lines in the brochure that draws attention to this. We us state of the art technology to produce high quality images efficiently, safely and economically. 

Thank you
Marisa

Reason: We need additional time to receive and review designs.

Reason: Need additional time to communicate with designers and to review changes. Thank you Marisa

I have extended the project date a few days. I have been incredibly impressed by the quality of your work and thank you all for your efforts.  I am waiting on a few revisions by a number of designers and look forward to receiving these changes.  We are close to completion.  Thanking you all again. Marisa 

Target Market(s)

We are targeting a wide range of industry sectors. Specifically, looking at targeting large engineering type consultancies, corporations, government agencies, auditing bodies. Typically, targeting the professional sector who use data to confirm, monitor and make better decisions.

We want the brochure design to be contemporary and modern which reflects what our business does. We use state of the art unmanned aerial technology to capture brilliant visual images and video. So we want our brochure to reflect that we're leaders in the field offering something different - cutting edge approach. I have additional photos that show vegetation mapping, wildlife surveys, agriculture and horticulture applications. Our services would benefit any business that uses visual data to help them make better, more informed decisions.

Industry/Entity Type

Business

Font styles to use
Serif
Sans Serif

Requirements
Must have
• We would like you to include photo of the UAV equipment/technology shots. This is new technology so we must also educate our clients on what our technology is capable of doing. We are offering a service that is very different so we want to be able to convey the true benefits of our services such as safety, efficiency, cost saving, reliability. We would like to convey these key themes. Credible data enables businesses to make better, faster decisions.
Nice to have
• We are essentially providing visual data in the form of high definition photos and videos. For this particular sector, data could be used for compliance or auditing purposes, planning, measuring, monitoring, evaluating, assessing, marketing. Could you please include these words in the brochure as they capture our service provision. Please note the red photo is infrared images.

```html
<!DOCTYPE html>
<html lang="en">
<head>
<meta charset="utf-8">
<title>Tremlow Skyworks – Environmental Compliance Brochure</title>
<link href="https://fonts.googleapis.com/css2?family=Arimo:wght@400;700&display=swap" rel="stylesheet">
<style>
:root{
  --canvas:#e8e5de;
  --green-deep:#0c4620;
  --green:#146b34;
  --green-mid:#1f8040;
  --green-light:#3d9c4f;
  --green-pale:#7fc28a;
  --ink:#ffffff;
  --blue:#2a8fd0;
}
*{margin:0;padding:0;box-sizing:border-box}
html,body{width:1200px;height:1000px;overflow:hidden;background:var(--canvas)}
body{position:relative;font-family:"Arimo",Arial,sans-serif;color:var(--ink)}
.page{position:absolute;top:245px;height:509px;overflow:hidden;box-shadow:0 6px 18px rgba(0,0,0,.25)}
.back-cover{left:45px;width:360px;background:linear-gradient(160deg,var(--green-mid),var(--green) 45%,var(--green-deep))}
.spread{left:435px;width:720px;background:linear-gradient(180deg,var(--green-mid),var(--green) 50%,var(--green-deep))}
.page svg.shapes{position:absolute;left:0;top:0}
.contact{position:absolute;left:40px;top:330px;width:290px;font-size:9px;line-height:1.25}
.contact-title{text-align:center;font-weight:700;font-size:10px}
.contact-intro{text-align:center;font-weight:700;margin-bottom:6px}
.contact-people{display:flex;gap:22px}
.contact-person{flex:1}
.contact-web{text-align:center;margin-top:12px;font-size:8px}
.col{position:absolute;font-size:6.6px;line-height:1.32}
.col p{margin-bottom:7px}
.col h3{font-size:7px;font-weight:700;letter-spacing:.3px;margin-bottom:5px}
.intro-col{left:14px;top:160px;width:156px}
.system-col{left:184px;top:16px;width:162px}
.services-col{left:378px;top:26px;width:150px}
.services-col h2{font-size:11px;font-weight:700;margin-bottom:8px}
.services-col p{font-size:10px;line-height:1.25;margin-bottom:12px}
.team-col{left:542px;top:14px;width:166px}
.team-col h3{margin-bottom:6px}
.team-col p{margin-bottom:6px}
.team-col .role{display:block}
</style>
</head>
<body>

<section class="page back-cover" aria-label="Back cover">
  <svg class="shapes" width="360" height="509" viewBox="0 0 360 509">
    <circle cx="180" cy="170" r="200" fill="#ffffff" opacity=".05"/>
    <circle cx="190" cy="200" r="150" fill="#ffffff" opacity=".06"/>
    <ellipse cx="175" cy="135" rx="135" ry="85" fill="#0e4f22" opacity=".55" role="img" aria-label="UAV drone illustration"/>
  </svg>
  <div class="contact">
    <div class="contact-title">CONTACT US</div>
    <div class="contact-intro">Find out more about our services by contacting:</div>
    <div class="contact-people">
      <div class="contact-person">
        <div>Daniel Ferris</div>
        <div>Principal Scientist</div>
        <div>61 3 9000 1234</div>
        <div>Mob: 0400 000 111</div>
        <div>daniel@tremlow.com.au</div>
      </div>
      <div class="contact-person">
        <div>Marisa Lindqvist</div>
        <div>Business Development Manager</div>
        <div>61 3 9000 1234</div>
        <div>Mob: 0400 222 333</div>
        <div>marisa@tremlow.com.au</div>
      </div>
    </div>
    <div class="contact-web">Find out more at www.tremlow.com.au</div>
  </div>
</section>

<section class="page spread" aria-label="Inside pages">
  <svg class="shapes" width="720" height="509" viewBox="0 0 720 509">
    <defs>
      <clipPath id="band-clip"><path d="M0,442 C200,512 450,372 720,277 L720,509 L0,509 Z"/></clipPath>
      <linearGradient id="photo-water" x1="0" y1="0" x2="1" y2="1"><stop offset="0" stop-color="#8fa7a5"/><stop offset="1" stop-color="#4f6b4e"/></linearGradient>
      <linearGradient id="photo-park" x1="0" y1="0" x2="1" y2="1"><stop offset="0" stop-color="#5f8d45"/><stop offset="1" stop-color="#33582c"/></linearGradient>
      <linearGradient id="photo-blossom" x1="0" y1="0" x2="1" y2="1"><stop offset="0" stop-color="#c9d3c2"/><stop offset="1" stop-color="#4e7a3c"/></linearGradient>
      <linearGradient id="photo-wetland" x1="0" y1="0" x2="1" y2="1"><stop offset="0" stop-color="#a9b3b1"/><stop offset="1" stop-color="#41653c"/></linearGradient>
    </defs>
    <circle cx="610" cy="110" r="150" fill="#ffffff" opacity=".06"/>
    <circle cx="20" cy="90" r="68" fill="var(--blue)" role="img" aria-label="UAV equipment photo"/>
    <circle cx="20" cy="90" r="68" fill="none" stroke="#ffffff" stroke-width="3"/>
    <path d="M0,430 C200,500 450,360 720,265" fill="none" stroke="var(--green-light)" stroke-width="12" opacity=".8"/>
    <g clip-path="url(#band-clip)">
      <rect x="0" y="250" width="170" height="260" fill="url(#photo-water)" role="img" aria-label="Aerial photo of coastal wetland"/>
      <rect x="170" y="250" width="170" height="260" fill="url(#photo-park)" role="img" aria-label="Aerial photo of parkland trees"/>
      <rect x="340" y="250" width="180" height="260" fill="url(#photo-blossom)" role="img" aria-label="Aerial photo of flowering vegetation"/>
      <rect x="520" y="250" width="200" height="260" fill="url(#photo-wetland)" role="img" aria-label="Aerial photo of levee and wetland ponds"/>
      <g stroke="#ffffff" stroke-width="2">
        <line x1="170" y1="250" x2="170" y2="509"/>
        <line x1="340" y1="250" x2="340" y2="509"/>
        <line x1="520" y1="250" x2="520" y2="509"/>
      </g>
    </g>
    <line x1="360" y1="0" x2="360" y2="509" stroke="#000" stroke-opacity=".15"/>
  </svg>

  <div class="col intro-col">
    <p>Tremlow is a company providing a range of services for over 20 years. We are a technology driven company using sophisticated technology to provide high quality environmental data and imaging solutions.</p>
    <p>There are many benefits associated with using UAV for environmental monitoring. UAV technology has revolutionized the way aerial spatial data is captured.</p>
    <p>Tremlow holds an Unmanned Aircraft System Operator's Certificate (UAS) issued by the aviation safety regulator. Our certification reflects our professionalism and commitment to high standards.</p>
    <p>Collectively, we have a wealth of knowledge and experience across a range of industry sectors. We have extensive experience in photographic, engineering and environmental science. Our team consists of highly regarded professionals who are passionate about what they do.</p>
    <p>By identifying our clients' needs, our process focuses on consultation. We work with our clients and business partners to determine how best we can add value to achieve efficient, quality outcomes.</p>
    <p>We are proud of our reputation and our ongoing commitment to provide our clients with aerial imaging that is professional, affordable and reliable.</p>
  </div>

  <div class="col system-col">
    <h3>TREMLOW UAV SYSTEM</h3>
    <p>Tremlow undertook extensive research to source the best fit for purpose UAV system currently available. Our UAV is mounted with a Veltra HD video camera and on-board GPS system. The video camera is image stabilised with 24megapixel photo capability. This level of resolution produces brilliant enlarged images that can be used for environmental data collection/monitoring, compliance and auditing purposes.</p>
    <p>The system is designed with GPS position hold function. This feature enables the pilot to lock the unit at specific positions and altitudes to capture the best possible image. The use of the GPS hold function in conjunction with the auto pilot software allows us to capture perfect repeat photography.</p>
    <p>Our sophisticated technology has 10 times zoom feature with the shutter controlled at ground level by the pilot. These functions enable still images and video to be recorded simultaneously. Camera angles are easily controlled whilst in flight. For mapping purposes, the camera can be pointed vertically to produce multiple stitched images.</p>
    <p>Our UAV system enables real time viewing via a wireless on-ground monitor. Tremlow's Chief Pilot is the only Environmental Scientist in Australia operating UAV commercially. As a Scientist, he has the technical expertise to analyse points of interest in real-time. Clients benefit from having all the data they need without visiting the site again. Our operations are always geared towards creating efficiency and cost savings for our clients.</p>
  </div>

  <div class="col services-col">
    <h2>OUR SERVICES:</h2>
    <p>As leaders in environmental science, we know how best to utilise UAV systems and technology. We have accumulated years of experience working with clients and applying knowledge to achieve sustainable results.</p>
    <p>We understand that collecting visual data using traditional aircraft is expensive, dangerous and time consuming. Tremlow provides a low cost, efficient solution that enables our clients to monitor, evaluate, manage and report on environmental change.</p>
  </div>

  <div class="col team-col">
    <h3>TREMLOW TEAM:</h3>
    <p>Daniel Ferris -<span class="role">Chief UAV Pilot and Environmental Scientist.</span>Daniel is the only environmental scientist in Australia certified by the aviation safety regulator to use UAV technology for commercial purposes. He is acknowledged nationally as an expert on the application and use of technology for environmental monitoring.</p>
    <p>He has over 20 years' experience in the environmental management sector including 15 years in the professional services industry.</p>
    <p>Marisa Lindqvist -<span class="role">Business Development &amp; Operations Manager.</span>Marisa manages client relations, marketing, systems development, quality assurance and OH&amp;S compliance.</p>
    <p>Marisa has held management roles in the corporate sector working for global companies such as Austral Airways, Kenmori Motors and Halberd Defence. She has worked in the field of human resources, employee relations and organisational development. She is one of few people in Australia to be accredited by Kenmori Motor Corporation as a Total Quality Management Facilitator &amp; Assessor.</p>
  </div>
</section>

</body>
</html>
```